Whimsical business cards and stationary for accessories and gifts company
Please use your design expertise!
Whimsical business cards and stationary for accessories and gifts company - Children
Creative Brief
Bright & Fun-filled
Marisa T Palvendo
Designer
Somerset, New Jersey
PipandLulaDesigns@brimletmail.com
www.PipAndLulaDesigns.craftvane.com www.friendloop.com/PipandLulaDesigns @PipAndLulaDesigns
Hair Accessories Party Favors Unique Gifts
Concepts
Business Cards for kids golf
Vanta Vanta
Kindly upload the Ai file of your logo.

```html
<!DOCTYPE html>
<html lang="en">
<head>
<meta charset="utf-8">
<title>Pip &amp; Lula business cards</title>
<link href="https://fonts.googleapis.com/css2?family=Raleway:wght@400;500;600&display=swap" rel="stylesheet">
<style>
  :root {
    --bg: #ece8ea;
    --purple: #9c3f98;
    --purple-deep: #8a3487;
    --purple-light: #b45aae;
    --purple-pale: #e7cfe5;
    --ink: #5a5a5a;
    --white: #ffffff;
  }
  * { margin: 0; padding: 0; box-sizing: border-box; }
  html, body { width: 1200px; height: 904px; overflow: hidden; background: var(--bg); }
  body { font-family: "Raleway", sans-serif; position: relative; }

  .card {
    position: absolute; left: 250px; width: 700px; height: 400px;
    border-radius: 4px; overflow: hidden;
    box-shadow: 0 6px 18px rgba(0,0,0,.18);
  }
  .card-back {
    top: 22px;
    background: linear-gradient(160deg, var(--purple-light), var(--purple) 55%, var(--purple-deep));
    color: var(--white);
  }
  .back-mark {
    position: absolute; left: 0; right: 0; top: 120px;
    display: flex; align-items: center; justify-content: center; gap: 14px;
  }
  .back-mark .dot { width: 22px; height: 22px; border-radius: 50%; background: rgba(255,255,255,.35); }
  .back-mark .name { font-size: 44px; font-weight: 500; color: rgba(255,255,255,.55); letter-spacing: 1px; }
  .services {
    position: absolute; left: 0; right: 0; bottom: 92px; text-align: center;
    font-size: 14px; letter-spacing: .5px; color: rgba(255,255,255,.9);
  }
  .services span { margin: 0 8px; }

  .card-front { top: 482px; background: var(--white); }
  .front-deco {
    position: absolute; right: -150px; top: 30px; width: 340px; height: 340px;
    border-radius: 50%; background: var(--purple-pale);
  }
  .brand { position: absolute; left: 40px; top: 48px; }
  .brand-row { display: flex; align-items: center; gap: 10px; }
  .brand .dot { width: 22px; height: 22px; border-radius: 50%; background: var(--purple); }
  .brand .name { font-size: 40px; font-weight: 500; color: var(--purple); line-height: 1; }
  .brand .tagline { margin: 4px 0 0 34px; font-size: 9px; color: var(--purple); letter-spacing: 1px; }

  .person { position: absolute; left: 40px; top: 188px; }
  .person .full-name { font-size: 19px; font-weight: 500; color: var(--purple); }
  .person .role { font-size: 13px; color: var(--ink); margin-top: 2px; }

  .contacts { position: absolute; left: 40px; top: 240px; list-style: none; }
  .contacts li { display: flex; align-items: center; gap: 10px; font-size: 13px; color: var(--ink); height: 17px; }
  .contacts .icon { width: 11px; height: 11px; border-radius: 2px; background: var(--purple); flex: none; }
  .contacts svg { flex: none; }
</style>
</head>
<body>
  <section class="card card-back" aria-label="Card back">
    <div class="back-mark">
      <span class="dot"></span>
      <span class="name">pip &amp; lula</span>
    </div>
    <p class="services"><span>Hair Accessories</span>|<span>Party Favors</span>|<span>Unique Gifts</span></p>
  </section>

  <section class="card card-front" aria-label="Card front">
    <div class="front-deco"></div>
    <div class="brand">
      <div class="brand-row">
        <span class="dot"></span>
        <span class="name">pip &amp; lula</span>
      </div>
      <p class="tagline">Whimsical Gifts Studio</p>
    </div>
    <div class="person">
      <p class="full-name">Marisa T Palvendo</p>
      <p class="role">Designer</p>
    </div>
    <ul class="contacts">
      <li>
        <svg width="11" height="11" viewBox="0 0 24 24" aria-hidden="true"><path fill="#9c3f98" d="M6.6 10.8a15 15 0 0 0 6.6 6.6l2.2-2.2a1 1 0 0 1 1-.25 11.4 11.4 0 0 0 3.6.57 1 1 0 0 1 1 1V20a1 1 0 0 1-1 1A17 17 0 0 1 3 4a1 1 0 0 1 1-1h3.5a1 1 0 0 1 1 1c0 1.25.2 2.45.57 3.6a1 1 0 0 1-.25 1z"/></svg>
        (555) 014-2287
      </li>
      <li><span class="icon"></span>PipandLulaDesigns@brimletmail.com</li>
      <li><span class="icon"></span>www.PipAndLulaDesigns.craftvane.com</li>
      <li><span class="icon"></span>www.friendloop.com/PipandLulaDesigns</li>
      <li><span class="icon"></span>@PipAndLulaDesigns</li>
    </ul>
  </section>
</body>
</html>
```